ZRD Roofing Billboard Design

Looking for a fresh new billboard design with my new headshot photo and using some info from my previous billboard and maybe website for design/content inspiration. My website is https://zrdroofing.com/

Also attached are my logo and current lawn sign design. I am looking for something simple, clean and modern. The landing page website should be 3816tops.com like my previous billboard has.

```html
<!DOCTYPE html>
<html lang="en">
<head>
<meta charset="UTF-8">
<title>ZRD Roofing Billboard</title>
<link href="https://fonts.googleapis.com/css2?family=Montserrat:ital,wght@0,600;0,700;0,800;1,900&display=swap" rel="stylesheet">
<style>
  :root {
    --navy: #243f5e;
    --navy-deep: #1d344f;
    --lime: #b9d431;
    --white: #ffffff;
    --sky: #3fb4e4;
    --roof-grey: #6c7a86;
  }
  html, body {
    margin: 0;
    padding: 0;
    overflow: hidden;
    background: #e9ecef;
  }
  .billboard {
    position: relative;
    width: 1200px;
    height: 353px;
    background: var(--navy);
    overflow: hidden;
    font-family: "Montserrat", sans-serif;
  }
  .roof-backdrop {
    position: absolute;
    left: 700px;
    top: 0;
    width: 500px;
    height: 273px;
    background: linear-gradient(90deg, var(--navy) 0%, #4a5c70 35%, #7b8793 70%, #8c96a0 100%);
  }
  .headshot {
    position: absolute;
    left: 834px;
    top: 24px;
    width: 340px;
    height: 249px;
    background: linear-gradient(180deg, #6e5a4d 0%, #b48a72 40%, #c9d3e6 75%, #d6def0 100%);
    border-radius: 140px 140px 0 0;
  }
  .price-band {
    position: absolute;
    left: 0;
    top: 273px;
    width: 1200px;
    height: 80px;
    background: var(--lime);
  }
  .roof-corner {
    position: absolute;
    left: 0;
    top: 242px;
    width: 580px;
    height: 111px;
    background: linear-gradient(90deg, #5d6770 0%, #66727b 55%, rgba(185,212,49,0.6) 80%, rgba(185,212,49,0) 100%);
    clip-path: polygon(0 55%, 46% 0, 54% 0, 80% 38%, 100% 38%, 100% 100%, 0 100%);
  }
  .headline {
    position: absolute;
    left: 35px;
    top: 22px;
    margin: 0;
    color: var(--lime);
    font-weight: 900;
    font-style: italic;
    font-size: 76px;
    line-height: 1;
    letter-spacing: -0.5px;
    white-space: nowrap;
  }
  .tagline {
    position: absolute;
    left: 39px;
    top: 99px;
    margin: 0;
    color: var(--white);
    font-weight: 900;
    font-style: italic;
    font-size: 47px;
    line-height: 1;
    white-space: nowrap;
  }
  .brand {
    position: absolute;
    left: 38px;
    top: 172px;
    display: flex;
    align-items: center;
    gap: 12px;
  }
  .brand-mark {
    width: 44px;
    height: 44px;
    border-radius: 50%;
    background: var(--lime);
  }
  .brand-name {
    color: var(--white);
    font-weight: 800;
    font-size: 30px;
    letter-spacing: 0.5px;
    white-space: nowrap;
  }
  .divider {
    position: absolute;
    left: 356px;
    top: 161px;
    width: 3px;
    height: 68px;
    background: var(--white);
  }
  .credentials {
    position: absolute;
    left: 397px;
    top: 166px;
    color: var(--white);
    font-weight: 600;
    font-size: 19px;
    letter-spacing: 1.4px;
    line-height: 1;
  }
  .rating {
    display: flex;
    align-items: center;
    gap: 6px;
  }
  .stars {
    display: flex;
    gap: 6px;
  }
  .stars svg {
    width: 18px;
    height: 18px;
    fill: var(--sky);
  }
  .licensed {
    margin-top: 12px;
  }
  .web-address {
    position: absolute;
    left: 628px;
    top: 278px;
    color: var(--navy);
    font-weight: 800;
    font-size: 66px;
    line-height: 1;
    letter-spacing: 0.5px;
    white-space: nowrap;
  }
</style>
</head>
<body>
  <main class="billboard">
    <div class="roof-backdrop" role="img" aria-label="Aerial photo of a grey shingle roof with a skylight"></div>
    <div class="headshot" role="img" aria-label="Headshot photo of the company owner in a light blue shirt"></div>
    <div class="price-band"></div>
    <div class="roof-corner" role="img" aria-label="Photo of a grey shingled roof peak"></div>

    <h1 class="headline">ROOF PROBLEMS?</h1>
    <p class="tagline">WE FIX IT RIGHT.</p>

    <div class="brand">
      <span class="brand-mark"></span>
      <span class="brand-name">ZRD ROOFING</span>
    </div>

    <div class="divider"></div>

    <div class="credentials">
      <div class="rating">
        <span class="stars" aria-label="Five stars">
          <svg viewBox="0 0 24 24"><polygon points="12,1.5 14.9,8.8 22.7,9.3 16.7,14.3 18.6,21.9 12,17.7 5.4,21.9 7.3,14.3 1.3,9.3 9.1,8.8"/></svg>
          <svg viewBox="0 0 24 24"><polygon points="12,1.5 14.9,8.8 22.7,9.3 16.7,14.3 18.6,21.9 12,17.7 5.4,21.9 7.3,14.3 1.3,9.3 9.1,8.8"/></svg>
          <svg viewBox="0 0 24 24"><polygon points="12,1.5 14.9,8.8 22.7,9.3 16.7,14.3 18.6,21.9 12,17.7 5.4,21.9 7.3,14.3 1.3,9.3 9.1,8.8"/></svg>
          <svg viewBox="0 0 24 24"><polygon points="12,1.5 14.9,8.8 22.7,9.3 16.7,14.3 18.6,21.9 12,17.7 5.4,21.9 7.3,14.3 1.3,9.3 9.1,8.8"/></svg>
          <svg viewBox="0 0 24 24"><polygon points="12,1.5 14.9,8.8 22.7,9.3 16.7,14.3 18.6,21.9 12,17.7 5.4,21.9 7.3,14.3 1.3,9.3 9.1,8.8"/></svg>
        </span>
        <span>5-STAR RATED</span>
      </div>
      <div class="licensed">LICENSED &amp; INSURED</div>
    </div>

    <div class="web-address">3816tops.com</div>
  </main>
</body>
</html>
```